Tallow & Mersey Needs New Stationery / Letterhead Design

We need new stationery to match our new logo (attached). Tallow & Mersey is a 34 year old nationwide law firm located in Houston Tx. They do personal injury law and pharmaceutical litigation.

WE DO NOT NEED BUSINESS CARDS.

Attached are several different file formats of the new logo.

Reason: We will make a decision in the next couple days. Finalizing edits now. Thank you!

Target Market(s)

consumers who have been injured due to the negligence of another or by a pharmaceutical drug or defective medical device. Also co-counsel and opposing counsel (law firms0.

Industry/Entity Type

Law Firm

Requirements
Must have
• logo
• Tallow & Mersey, LLP
• 7183 Corvid Lane, Suite 1000
• Brenford, TX 75591
• Tel: (555) 408-1936
• Fax: (555) 408-2275
• www.tallowandmersey.example
• Must have colors in the logo.
• Make the font go with the logo - not necessarily the same, but something that goes well with it.

```html
<!DOCTYPE html>
<html lang="en">
<head>
<meta charset="utf-8">
<title>Tallow &amp; Mersey Stationery</title>
<link href="https://fonts.googleapis.com/css2?family=Open+Sans:wght@400;600;700&family=Oswald:wght@500&family=Titillium+Web:wght@600&family=Dancing+Script:wght@500&display=swap" rel="stylesheet">
<style>
:root{
  --navy:#0d2f55;
  --navy-deep:#082443;
  --navy-mid:#1d4a80;
  --band-grey:#3a3b3d;
  --teal:#66c9c4;
  --teal-pale:#e6f6f5;
  --paper:#ffffff;
  --ink:#222;
  --backdrop:#e8e4de;
}
*{margin:0;padding:0;box-sizing:border-box}
html,body{width:1200px;height:720px;overflow:hidden}
body{background:var(--backdrop);position:relative;font-family:"Open Sans",Arial,sans-serif;color:var(--ink)}
.sheet{position:absolute;background:var(--paper);box-shadow:0 2px 6px rgba(0,0,0,.18);overflow:hidden}

/* showcase heading */
.showcase-title{position:absolute;left:424px;top:72px;width:409px;text-align:center;color:var(--navy)}
.showcase-title .lead{font-family:"Titillium Web",sans-serif;font-weight:600;font-size:36px;line-height:1}
.showcase-title .main{font-family:"Oswald",sans-serif;font-weight:500;font-size:48px;line-height:1.05;letter-spacing:.5px}

/* firm name lockup */
.firm-mark{display:flex;align-items:center;gap:6px;color:var(--navy);font-family:"Open Sans",sans-serif;font-weight:700;white-space:nowrap}
.firm-mark .mark-square{background:var(--navy);flex:none}

/* letterhead */
.letterhead{left:10px;top:75px;width:390px;height:550px}
.letterhead .rule-top{position:absolute;left:0;top:0;width:100%;height:8px;background:var(--navy)}
.letterhead .band-top{position:absolute;left:0;top:8px;width:100%;height:20px;background:var(--band-grey)}
.letterhead .header-tab{position:absolute;left:134px;top:4px;width:124px;height:26px;background:var(--paper);border-radius:8px 8px 0 0;display:flex;justify-content:center;align-items:center}
.letterhead .header-tab .firm-mark{font-size:9px;gap:4px}
.letterhead .header-tab .mark-square{width:8px;height:8px}
.letter-body{position:absolute;left:45px;top:110px;width:300px;font-size:7px;line-height:9px}
.letter-body p{margin-bottom:8px;text-align:justify}
.letter-body .recipient{text-align:left}
.signature{font-family:"Dancing Script",cursive;color:var(--navy-mid);font-size:10px;line-height:11px;margin-top:26px}
.sender{text-align:left}
.letter-footer{position:absolute;left:0;bottom:0;width:100%;height:38px;background:linear-gradient(90deg,var(--navy-deep),var(--navy-mid) 60%,var(--navy-deep))}
.footer-icon{position:absolute;top:-9px;width:18px;height:18px;border-radius:50%;background:var(--paper);border:1.5px solid var(--navy);display:flex;align-items:center;justify-content:center}
.footer-icon svg{width:10px;height:10px}
.footer-text{position:absolute;top:13px;color:#fff;font-size:6px;line-height:7px;font-weight:700;white-space:nowrap}
.footer-text.address{top:12px;font-size:5.5px;line-height:7px}

/* envelopes */
.envelope{left:424px;width:409px;height:205px;background:linear-gradient(170deg,#fff 10%,var(--teal-pale) 40%,var(--teal) 100%)}
.envelope-front{top:192px;border:1px solid #b7c9d8}
.envelope-back{top:419px}
.envelope .decor{position:absolute;inset:0}
.envelope-front .firm-mark{position:absolute;left:22px;top:62px;font-size:17px;gap:8px}
.envelope-front .mark-square{width:16px;height:16px}
.address-window{position:absolute;left:206px;top:88px;width:166px;height:82px;background:#fff;border:1px solid #d4dde4;box-shadow:0 1px 3px rgba(0,0,0,.15)}
.address-window span{position:absolute;left:18px;width:130px;height:1px;background:#777}
.envelope-back .firm-mark{position:absolute;left:0;right:0;top:108px;justify-content:center;font-size:17px;gap:8px}
.envelope-back .mark-square{width:16px;height:16px}

/* notepad */
.notepad{left:854px;top:232px;width:279px;height:390px;background:linear-gradient(180deg,var(--teal) 0%,var(--teal-pale) 28%,#fff 42%)}
.notepad .decor{position:absolute;left:0;top:0;width:100%;height:90px}
.notepad .binding{position:absolute;left:0;top:-2px;width:100%;height:22px}
.notepad .firm-mark{position:absolute;left:0;right:0;top:210px;justify-content:center;font-size:15px;gap:7px}
.notepad .mark-square{width:14px;height:14px}
.pad-footer{position:absolute;left:4px;right:4px;bottom:5px;height:19px;border-top:1px solid var(--navy)}
.pad-footer .stripe{position:absolute;left:0;top:0;width:96px;height:15px;background:var(--navy);clip-path:polygon(0 0,100% 0,88% 100%,0 100%)}
.pad-footer span{position:absolute;top:2px;font-size:4px;line-height:5px;white-space:nowrap}
</style>
</head>
<body>

<div class="showcase-title">
  <div class="lead">Tallow &amp; Mersey’s</div>
  <div class="main">STATIONERY DESIGN</div>
</div>

<!-- letterhead -->
<section class="sheet letterhead">
  <div class="rule-top"></div>
  <div class="band-top"></div>
  <div class="header-tab">
    <div class="firm-mark"><span class="mark-square"></span>Tallow &amp; Mersey</div>
  </div>
  <div class="letter-body">
    <p>Dec 17, 2016</p>
    <p class="recipient">First Last Name<br>Street Address<br>City, State 00000</p>
    <p>Dear :</p>
    <p>Lorem ipsum dolor sit amet, consectetur adipiscing elit. Aenean ut ipsum eget massa hendrerit vestibulum vel in velit. Donec pretium neque velit.</p>
    <p>Aliquam porta lectus nec mauris ornare venenatis. Vivamus non est turpis, et cursus sem. Mauris vehicula erat in diam auctor at bibendum nisl lacinia.</p>
    <p>Morbi imperdiet neque vehicula nunc convallis gravida. Vestibulum iac ulis pretium pl acerat. Integer consequat, est sit amet facilisis eleifend, nibh nibh varius orci, eget dap ibus arcu dui non purus. Pellentesque in magna mauris. Duis enim sapien, dictum vitae condimentum a, pulvinar vel lacus. Mauris et molestie nibh. Vestibulum vitae nulla at metus elementum porta sit amet interdum elit. Nulla sollicitudin neque eu nulla volutpat congue.</p>
    <p>Etiam pellentesque, velit id dapibus fermentum, turpis sapien ornare dui, ac tincidunt ligula odio congue purus. Nunc sed ante dui, in porta lectus. Cras nec sem lorem. In hac habitasse platea dictumst. Maecenas id diam quis dui porta tristique. Sed id egestas felis. Donec ullamcorper mattis posuere. Phasellus fermentum eleifend tortor vel da pibus. Vestibulum ante ipsum.</p>
    <p class="recipient">Sincerely,</p>
    <div class="signature">Daniel Wrenfield</div>
    <p class="sender">YourOffice.example<br>P.O. Box 000000<br>Ashford, CO 80000<br>P: (012) 345-6789</p>
  </div>
  <footer class="letter-footer">
    <div class="footer-icon" style="left:83px">
      <svg viewBox="0 0 24 24"><path fill="var(--navy)" d="M6.6 10.8a15 15 0 0 0 6.6 6.6l2.2-2.2c.3-.3.7-.4 1-.2 1.1.4 2.3.6 3.6.6.6 0 1 .4 1 1V20c0 .6-.4 1-1 1A17 17 0 0 1 3 4c0-.6.4-1 1-1h3.5c.6 0 1 .4 1 1 0 1.3.2 2.5.6 3.6.1.3 0 .7-.2 1z"/></svg>
    </div>
    <div class="footer-icon" style="left:186px">
      <svg viewBox="0 0 24 24"><g fill="none" stroke="var(--navy)" stroke-width="2.4" stroke-linecap="round"><path d="M10 14l4-4"/><path d="M9 11l-2 2a3 3 0 0 0 4 4l2-2"/><path d="M15 13l2-2a3 3 0 0 0-4-4l-2 2"/></g></svg>
    </div>
    <div class="footer-icon" style="left:289px">
      <svg viewBox="0 0 24 24"><path fill="var(--navy)" d="M12 2a7 7 0 0 0-7 7c0 5 7 13 7 13s7-8 7-13a7 7 0 0 0-7-7zm0 9.5A2.5 2.5 0 1 1 12 6.5a2.5 2.5 0 0 1 0 5z"/></svg>
    </div>
    <div class="footer-text" style="left:62px">Tel: &nbsp;(555) 408-1936<br>Fax: (555) 408-2275</div>
    <div class="footer-text" style="left:154px">www.tallowandmersey.example<br>info@tallowandmersey.example</div>
    <div class="footer-text address" style="left:279px">Tallow &amp; Mersey, LLP<br>7183 Corvid Lane, Suite 1000<br>Brenford, TX 75591</div>
  </footer>
</section>

<!-- envelope front -->
<section class="sheet envelope envelope-front">
  <svg class="decor" viewBox="0 0 409 205" preserveAspectRatio="none" aria-hidden="true">
    <defs>
      <linearGradient id="swoopFront" x1="0" x2="1">
        <stop offset="0" stop-color="#0a2a52"/><stop offset=".6" stop-color="#1d4c86"/><stop offset="1" stop-color="#0d2f55"/>
      </linearGradient>
    </defs>
    <path d="M0 158 C90 190 220 196 409 150 L409 205 L0 205Z" fill="url(#swoopFront)"/>
    <path d="M0 148 C100 186 230 190 330 186 C240 198 110 192 0 160Z" fill="#fff" opacity=".95"/>
  </svg>
  <div class="firm-mark"><span class="mark-square"></span>Tallow &amp; Mersey</div>
  <div class="address-window">
    <span style="top:44px"></span><span style="top:53px"></span><span style="top:62px"></span><span style="top:71px"></span>
  </div>
</section>

<!-- envelope back -->
<section class="sheet envelope envelope-back">
  <svg class="decor" viewBox="0 0 409 205" preserveAspectRatio="none" aria-hidden="true">
    <defs>
      <linearGradient id="swoopBack" x1="0" x2="1">
        <stop offset="0" stop-color="#0a2a52"/><stop offset=".6" stop-color="#1d4c86"/><stop offset="1" stop-color="#0d2f55"/>
      </linearGradient>
    </defs>
    <path d="M0 0 H409 V58 C409 64 405 66 398 66 H10 C4 66 0 63 0 58Z" fill="#0b2c53"/>
    <path d="M8 0 V50 C8 56 12 58 18 58 H392 C398 58 401 55 401 50 V0" fill="none" stroke="#4f86b5" stroke-width="1.2"/>
    <path d="M0 160 C90 190 220 196 409 152 L409 205 L0 205Z" fill="url(#swoopBack)"/>
    <path d="M0 150 C100 188 230 192 320 188 C230 200 110 194 0 162Z" fill="#fff" opacity=".95"/>
  </svg>
  <div class="firm-mark"><span class="mark-square"></span>Tallow &amp; Mersey</div>
</section>

<!-- notepad -->
<section class="sheet notepad">
  <svg class="decor" viewBox="0 0 279 90" preserveAspectRatio="none" aria-hidden="true">
    <path d="M0 0 H279 V24 C200 10 90 12 0 30Z" fill="#0d2f55"/>
    <path d="M0 34 C90 16 200 14 279 34 V38 C200 20 90 22 0 40Z" fill="#fff"/>
  </svg>
  <svg class="binding" viewBox="0 0 279 22" aria-hidden="true">
    <g fill="none" stroke="#c9ced4" stroke-width="2">
      <path d="M16 20 V4"/><path d="M42 20 V4"/><path d="M68 20 V4"/><path d="M94 20 V4"/><path d="M120 20 V4"/><path d="M146 20 V4"/><path d="M172 20 V4"/><path d="M198 20 V4"/><path d="M224 20 V4"/><path d="M250 20 V4"/>
    </g>
    <g fill="#0a2442">
      <circle cx="16" cy="20" r="2.5"/><circle cx="42" cy="20" r="2.5"/><circle cx="68" cy="20" r="2.5"/><circle cx="94" cy="20" r="2.5"/><circle cx="120" cy="20" r="2.5"/><circle cx="146" cy="20" r="2.5"/><circle cx="172" cy="20" r="2.5"/><circle cx="198" cy="20" r="2.5"/><circle cx="224" cy="20" r="2.5"/><circle cx="250" cy="20" r="2.5"/>
    </g>
  </svg>
  <div class="firm-mark"><span class="mark-square"></span>Tallow &amp; Mersey</div>
  <div class="pad-footer">
    <div class="stripe"></div>
    <span style="left:5px;color:#fff;font-weight:700">Tel: (555) 408-1936<br>Fax: (555) 408-2275</span>
    <span style="left:108px">www.tallowandmersey.example<br>info@tallowandmersey.example</span>
    <span style="right:4px;text-align:right">Tallow &amp; Mersey, LLP<br>7183 Corvid Lane, Suite 1000<br>Brenford, TX 75591</span>
  </div>
</section>

</body>
</html>
```